Sales and Marketing company needs website page graphics

We are redesigning our website and need graphics for the top of our solution pages. Currently you’ll see that there is one photo graphic with a differing color screen for each section. We’re looking for photo graphic designs that will represent each unique solution section (lead generation, prospecting, hiring) and fit within the overall website design. We will add the section title text to the photo graphic. This will be a total of 3 graphics.

This is a link to the working website redesign: http://brivotelnet.com/zumaplexdraft/
The content on the working redesign page is correct and will give you a good sense for how we talk about each solution. You’ll notice that the redesign is text heavy. We’ll work on that next.

Our current website is: www.zumaplex.com
You’ll get a good sense for our designs on our blog: http://www.zumaplex.com/blog

As a company, our goal is to help our clients get more customers. We do that through consulting, training and outsourced lead generation. Key words that describe us: flexible, responsive, and fun. (Although you don’t see that in our current website, hopefully it comes through more on our blog – and then on our new website!)

We will need the graphic design in high resolution formats. We will own the copyright and intellectual property.

Target Market(s)

North American companies that earn $750K - $85M in annual revenue selling to other businesses. Most are in the computer technology industry.

Industry/Entity Type

Business Service

Font styles to use
Sans Serif

Requirements
Must have
• Fit the design of the website.
• If there are people in the graphics, I like to see diversity: Asian,Black, Latin, Caucasian, men and women.
Nice to have
• Be creative, not like every other graphic you see on a website. We are a woman owned business and Marisol is well known. We don't want to feel generic. Potentially be something we can use elements of for other graphics.
Should not have
• We really want your expertise and this is our first project with ArtHiveNet .
• We will insert the solution section text, so there wouldn't be the text unless it's part of the graphic design.

```html
<!DOCTYPE html>
<html lang="en">
<head>
<meta charset="utf-8">
<title>Get More Sales Leads?</title>
<link href="https://fonts.googleapis.com/css2?family=Montserrat:wght@700;800&display=swap" rel="stylesheet">
<style>
  :root {
    --sky-light: #eee3f5;
    --sky-mid: #d7bfe6;
    --lilac: #b98fd2;
    --violet: #9a63bd;
    --plum: #6d3f92;
    --plum-deep: #3b1f5e;
    --suit: #4a2a78;
    --skin-glow: #f6c2dc;
    --flare: #ffffff;
    --ink: #0c0510;
    --white: #ffffff;
    --band: rgba(255, 255, 255, 0.24);
  }
  html, body {
    margin: 0;
    padding: 0;
    width: 1200px;
    height: 893px;
    overflow: hidden;
    background: var(--white);
  }
  .hero {
    position: relative;
    width: 1200px;
    height: 893px;
    overflow: hidden;
    font-family: "Montserrat", Arial, sans-serif;
    background: linear-gradient(180deg, var(--sky-light) 0%, var(--sky-mid) 38%, var(--lilac) 60%, var(--violet) 80%, var(--plum) 100%);
  }
  .hero-photo {
    position: absolute;
    inset: 0;
  }
  .photo-sky-flare {
    position: absolute;
    left: 520px;
    top: -120px;
    width: 300px;
    height: 260px;
    border-radius: 50%;
    background: radial-gradient(closest-side, var(--flare) 0%, rgba(255,255,255,0.7) 45%, rgba(255,255,255,0) 100%);
  }
  .photo-city {
    position: absolute;
    left: 0;
    top: 470px;
    width: 1200px;
    height: 423px;
    background: linear-gradient(180deg, rgba(109,63,146,0) 0%, rgba(109,63,146,0.35) 40%, rgba(80,40,120,0.6) 100%);
  }
  .photo-sketches {
    position: absolute;
    left: 110px;
    top: 230px;
    width: 560px;
    height: 400px;
    border-radius: 40%;
    background: radial-gradient(closest-side, rgba(120,60,150,0.28) 0%, rgba(120,60,150,0.12) 60%, rgba(120,60,150,0) 100%);
  }
  .photo-suit {
    position: absolute;
    left: 480px;
    top: -40px;
    width: 640px;
    height: 980px;
    border-radius: 42% 30% 8% 20%;
    background: linear-gradient(100deg, rgba(120,80,170,0.45) 0%, rgba(74,42,120,0.85) 40%, rgba(59,31,94,0.92) 75%, rgba(90,55,140,0.6) 100%);
    filter: blur(18px);
  }
  .photo-hand {
    position: absolute;
    left: 690px;
    top: 300px;
    width: 320px;
    height: 330px;
    border-radius: 45% 50% 40% 55%;
    background: radial-gradient(ellipse at 40% 55%, var(--skin-glow) 0%, rgba(232,160,205,0.85) 45%, rgba(200,120,180,0) 100%);
    filter: blur(10px);
  }
  .growth-chart {
    position: absolute;
    inset: 0;
    width: 1200px;
    height: 893px;
  }
  .headline-lead {
    position: absolute;
    left: 118px;
    top: 617px;
    margin: 0;
    font-size: 60px;
    font-weight: 700;
    line-height: 1;
    color: var(--ink);
    letter-spacing: -0.5px;
    white-space: nowrap;
  }
  .headline-band {
    position: absolute;
    left: 83px;
    top: 702px;
    width: 1000px;
    height: 130px;
    background: var(--band);
  }
  .headline-main {
    position: absolute;
    left: 118px;
    top: 713px;
    margin: 0;
    font-size: 110px;
    font-weight: 800;
    line-height: 1;
    color: var(--white);
    letter-spacing: 1px;
    white-space: nowrap;
  }
</style>
</head>
<body>
  <main class="hero">
    <div class="hero-photo" role="img" aria-label="Purple-toned photo of a businessman in a dark suit pointing his finger forward over a hazy city skyline, with hand-drawn business sketches of charts, ideas and teams floating beside him">
      <div class="photo-sky-flare"></div>
      <div class="photo-city"></div>
      <div class="photo-sketches"></div>
      <div class="photo-suit"></div>
      <div class="photo-hand"></div>
    </div>

    <svg class="growth-chart" viewBox="0 0 1200 893" aria-hidden="true">
      <polyline points="53,559 127,448 207,527 315,382 416,497 506,406 613,427 712,300"
                fill="none" stroke="#ffffff" stroke-width="4" stroke-linejoin="round" stroke-linecap="round"/>
      <g fill="#ffffff">
        <circle cx="53" cy="559" r="7"/>
        <circle cx="127" cy="448" r="7"/>
        <circle cx="207" cy="527" r="7"/>
        <circle cx="315" cy="382" r="7"/>
        <circle cx="416" cy="497" r="7"/>
        <circle cx="506" cy="406" r="7"/>
        <circle cx="613" cy="427" r="7"/>
      </g>
    </svg>

    <h2 class="headline-lead">Get More</h2>
    <div class="headline-band"></div>
    <h1 class="headline-main">SALES LEADS?</h1>
  </main>
</body>
</html>
```